Billboard design for a small town Oral Surgeon

We are getting several billboards and need a design that highlights the doctors photo, and bullet points of what he does. Our business name is extremely long, so it’s a challenge to figure out how to do this. Maybe just use our logo? Open to ideas.
The logo can be shortened as designer sees fit, meaning we can drop the tag line. Important info to include:
Doctors name is Lorvik Tamsen
The highlighted bullet points are:
•Implants
•wisdom teeth
•Jaw Surgery
•facial trauma
The goal of this billboard is to let our community know that they have an option here in Ada, our town. Many still drive to the city a couple hours away not knowing they now have an option here at home. Having a hard time finding examples of what I have in mind, so hoping this will get us going. I want it as “non-busy” as possible, so no unnecessary lines or anything that competes with the information we are trying to get across.

Target Market(s)

Everyone in town, just trying to spread the word that we are here

Industry/Entity Type

Medical/surgical (oral surgery)

Font styles to use
Sans Serif

Colors
0094D4
00A9DD
6FCCEA
C7EBF8
E9F6FB

Requirements
Must have
• *New note** Due to location of billboard, I prefer the photo of doctor to be on the left side. Must look neat and professional. Must highlight what we do.
Nice to have
• Our colors are a blue-green with silver, against black or white, but I’m flexible on this, I don’t necessarily need the colors highlighted. I’m also flexible on font style, just needs to be easy to read.
Should not have
• Distracting graphics, should not look like a dental office. That’s an issue we have is people thinking we are another dental office, we do not do any general dentistry, it’s surgery only.

```html
<!DOCTYPE html>
<html lang="en">
<head>
<meta charset="utf-8">
<title>Redbud Valley Oral &amp; Maxillofacial Surgery – Billboard</title>
<link rel="stylesheet" href="https://fonts.googleapis.com/css2?family=Playfair+Display:wght@900&family=Great+Vibes&family=Roboto+Condensed:wght@700&family=Raleway:wght@400;500&display=swap">
<style>
  :root {
    --stage: #000000;
    --board: #ffffff;
    --teal: #1791aa;
    --ink: #0a0a0a;
    --silver: #9a9a9c;
    --photo-light: #5a5d62;
    --photo-dark: #1b1d21;
    --band-shade: rgba(0, 20, 40, 0.55);
  }
  * { margin: 0; padding: 0; box-sizing: border-box; }
  html, body {
    width: 1200px; height: 1000px; overflow: hidden;
    background: var(--stage);
  }
  .billboard {
    position: absolute; left: 101px; top: 334px;
    width: 998px; height: 333px;
    background: var(--board);
  }
  .brand {
    position: absolute; left: 35px; top: 42px; width: 176px;
    text-align: center;
  }
  .brand-mark {
    display: block; margin: 0 auto 14px;
    width: 76px; height: 76px; border-radius: 50%;
    border: 3px solid var(--silver);
  }
  .brand-name {
    font-family: "Raleway", sans-serif; font-weight: 400;
    font-size: 12.4px; line-height: 15px; color: var(--ink);
    text-align: left; letter-spacing: -0.2px;
    padding-bottom: 4px; border-bottom: 1px solid var(--ink);
  }
  .brand-tagline {
    font-family: "Raleway", sans-serif; font-weight: 500;
    font-size: 6.6px; letter-spacing: 2.1px; color: var(--ink);
    text-align: left; margin-top: 4px; white-space: nowrap;
  }
  .name-band {
    position: absolute; left: 227px; top: 213px;
    width: 305px; height: 72px; background: var(--teal);
  }
  .portrait {
    position: absolute; left: 248px; top: 29px;
    width: 196px; height: 274px;
    background: radial-gradient(ellipse at 50% 35%, var(--photo-light) 0%, var(--photo-dark) 75%);
  }
  .portrait-band {
    position: absolute; left: 248px; top: 213px;
    width: 196px; height: 72px; background: var(--band-shade);
  }
  .doctor-name {
    position: absolute; left: 451px; top: 220px; width: 78px;
    font-family: "Roboto Condensed", sans-serif; font-weight: 700;
    color: var(--board); line-height: 1; white-space: nowrap;
  }
  .doctor-name .title { font-size: 17px; display: block; }
  .doctor-name .first { font-size: 25px; display: block; margin-top: 2px; letter-spacing: -0.3px; }
  .doctor-name .last { font-size: 18px; display: block; margin-top: 2px; }
  .headline {
    position: absolute; left: 536px; top: 36px;
    line-height: 1;
  }
  .headline-top {
    font-family: "Playfair Display", serif; font-weight: 900;
    font-size: 42px; color: var(--teal); letter-spacing: -0.5px;
    display: block;
  }
  .headline-bottom { display: block; margin-top: -4px; white-space: nowrap; }
  .headline-script {
    font-family: "Great Vibes", cursive; font-size: 34px; color: var(--ink);
    vertical-align: 22px;
  }
  .headline-main {
    font-family: "Playfair Display", serif; font-weight: 900;
    font-size: 80px; color: var(--ink); letter-spacing: -1px;
    margin-left: 4px;
  }
  .services {
    position: absolute; left: 623px; top: 159px;
    list-style: none;
    font-family: "Roboto Condensed", sans-serif; font-weight: 700;
    font-size: 27px; color: var(--ink); line-height: 37px;
  }
  .services li { display: flex; align-items: center; }
  .services svg { width: 8px; height: 10px; margin-right: 5px; flex: none; }
</style>
</head>
<body>
  <main class="billboard">
    <section class="brand">
      <span class="brand-mark"></span>
      <p class="brand-name">REDBUD VALLEY ORAL &amp; MAXILLOFACIAL SURGERY</p>
      <p class="brand-tagline">COMFORT | CARE | COMPASSION</p>
    </section>

    <div class="name-band"></div>
    <div class="portrait" role="img" aria-label="Portrait photograph of Dr. Lorvik Tamsen in a dark suit against a grey studio backdrop"></div>
    <div class="portrait-band"></div>
    <p class="doctor-name">
      <span class="title">DR.</span>
      <span class="first">LORVIK</span>
      <span class="last">TAMSEN</span>
    </p>

    <h1 class="headline">
      <span class="headline-top">WE RESTORING</span>
      <span class="headline-bottom"><span class="headline-script">Your</span><span class="headline-main">SMILES</span></span>
    </h1>

    <ul class="services">
      <li><svg viewBox="0 0 8 10"><polygon points="0,0 8,5 0,10" fill="var(--teal)"/></svg>IMPLANTS</li>
      <li><svg viewBox="0 0 8 10"><polygon points="0,0 8,5 0,10" fill="var(--teal)"/></svg>WISDOM TEETH</li>
      <li><svg viewBox="0 0 8 10"><polygon points="0,0 8,5 0,10" fill="var(--teal)"/></svg>JAW SURGERY</li>
      <li><svg viewBox="0 0 8 10"><polygon points="0,0 8,5 0,10" fill="var(--teal)"/></svg>FACIAL TRAUMA</li>
    </ul>
  </main>
</body>
</html>
```